Woman owned consulting company needs an elegant and modern business card design

I need a business card design for my new consulting company, Mira Holcombe Consulting. I am looking for something that is simple and elegant, but also creative and original. You can use either version of the logo that are attached. I have also included the information that needs to be featured on the business card.

Contact Information for Business Card

Requirements
Must have
• The logo and the font type and a standard business card size. Use shades of gray/silver and or rose gold that are in the logo.
• I didn't realize that my actual logo wasn't attached. Please incorporate in the designs.
Should not have
• Colors that are different from my logo

```html
<!DOCTYPE html>
<html lang="en">
<head>
<meta charset="utf-8">
<title>Mira Holcombe Consulting – Business Card</title>
<link href="https://fonts.googleapis.com/css2?family=Cinzel:wght@400;500&family=Crimson+Text:wght@400&display=swap" rel="stylesheet">
<style>
  :root {
    --page-bg: #c9c9c9;
    --card-dark: #3a3e41;
    --card-light: #f4f4f3;
    --silver: #d8d8d8;
    --silver-muted: #9c9c9c;
    --ink: #2b2b2b;
    --ink-soft: #4a4a4a;
  }
  * { margin: 0; padding: 0; box-sizing: border-box; }
  html, body {
    width: 1200px; height: 852px; overflow: hidden;
    background: var(--page-bg);
  }
  .stage {
    position: relative; width: 1200px; height: 852px;
    display: flex; align-items: center; justify-content: center; gap: 60px;
  }
  .card {
    position: relative; width: 500px; height: 286px;
    border-radius: 16px;
    box-shadow: 0 6px 18px rgba(0,0,0,0.18);
  }
  .card--front {
    background: var(--card-dark);
    display: flex; align-items: center; justify-content: center; gap: 16px;
  }
  .brand-mark {
    width: 12px; height: 12px; background: var(--silver);
  }
  .brand-name {
    font-family: "Cinzel", serif; font-weight: 400;
    color: var(--silver); font-size: 24px; line-height: 1.1;
    letter-spacing: 0.5px;
  }
  .brand-name small { display: block; font-size: 17px; }
  .card--back { background: var(--card-light); }
  .person {
    position: absolute; left: 40px; top: 46px;
  }
  .person__name {
    font-family: "Cinzel", serif; font-weight: 500;
    font-size: 18px; color: var(--ink); letter-spacing: 0.5px;
  }
  .person__role {
    font-family: "Crimson Text", serif; font-size: 12px; color: var(--ink-soft);
  }
  .back-brand {
    position: absolute; right: 36px; top: 50px;
    display: flex; align-items: center; gap: 8px;
    font-family: "Crimson Text", serif; font-weight: 400;
    font-size: 15px; color: var(--ink-soft);
  }
  .back-brand__square {
    width: 9px; height: 9px; background: var(--silver-muted);
  }
  .contact {
    position: absolute; left: 40px; bottom: 34px;
    font-family: "Crimson Text", serif; font-size: 13px; color: var(--ink-soft);
  }
  .contact__company {
    font-family: "Cinzel", serif; font-size: 13px; color: var(--ink);
    margin-bottom: 6px;
  }
  .contact__row { display: flex; align-items: center; gap: 9px; line-height: 19px; }
  .contact__icon { width: 11px; height: 11px; fill: var(--ink); }
  .contact__icon--line { fill: none; stroke: var(--ink); stroke-width: 1.2; }
</style>
</head>
<body>
<main class="stage">
  <section class="card card--front" aria-label="Card front">
    <span class="brand-mark"></span>
    <div class="brand-name">Mira Holcombe<small>Consulting, LLC</small></div>
  </section>

  <section class="card card--back" aria-label="Card back">
    <div class="person">
      <p class="person__name">Mira Holcombe</p>
      <p class="person__role">Owner</p>
    </div>
    <div class="back-brand">
      <span class="back-brand__square"></span>
      <span>Mira Holcombe</span>
    </div>
    <div class="contact">
      <p class="contact__company">Mira Holcombe Consulting, LLC</p>
      <p class="contact__row">
        <svg class="contact__icon" viewBox="0 0 12 12"><path d="M2.5 1h2l1 3-1.3 1a7 7 0 0 0 2.8 2.8L8 6.5l3 1v2A1.5 1.5 0 0 1 9.5 11 8.5 8.5 0 0 1 1 2.5 1.5 1.5 0 0 1 2.5 1z"/></svg>
        555-014-2273
      </p>
      <p class="contact__row">
        <svg class="contact__icon contact__icon--line" viewBox="0 0 12 12"><path d="M0.6 2.2h10.8v7.6H0.6z M1 3l5 4 5-4"/></svg>
        mira@miraholcombe.com
      </p>
      <p class="contact__row">
        <svg class="contact__icon" viewBox="0 0 12 12"><circle cx="6" cy="6" r="5.4"/><path d="M0.8 6h10.4M6 0.6v10.8M6 0.6c-3 3-3 7.8 0 10.8M6 0.6c3 3 3 7.8 0 10.8" fill="none" stroke="#f4f4f3" stroke-width="0.8"/></svg>
        www.miraholcombe.com
      </p>
    </div>
  </section>
</main>
</body>
</html>
```